Flyer für Vermieter von Monteursunterkünften
Zielgruppe
Guten Tag,
wir sind eine Fima, die Monteursunterkünfte vermietet. Wir vermieten möblierte Wohnungen auf Zeit. Man kann diese buchen ab 5 Tagen bis hin zu mehreren Monaten. Sie sind für Monteure, Handwerker oder Zeitarbeiter geeignet. Die Website dient lediglich zur Inspiration für Design und Farben. Auf der Website sprechen wir eine andere Zielgruppe an.
Mit den Flyern möchten wir Handwerksbetriebe oder auch Handwerker direkt ansprechen, welche auf der Suche nach einer günstigen und möblierten Unterkunft auf Zeit sind.
Es sollen beide Logos von der QT Dwelling und der RuhOrt17 verwendet werden.
Aufgabenstellung
Sie sind auf der Suche nach einer günstigen und komfortablen Unterkunft für Ihre Mitarbeiter? Dann sind Sie bei uns genau richtig!
BUCHEN Sie JETZT SCHNELL und EINFACH: 01629 581706
• Moderne und komfortable Wohnungen
• TV und Kühlschränke auf jedem Zimmer
• Voll ausgestattete Küche
• Immer mit Balkon oder Terrasse
• Kostenloses schnelles W-Lan
• Gute Parkmöglichkeiten
• Willkommenspaket
Überzeugen Sie sich selbst von unserem Angebot und buchen Sie noch heute eines unserer Monteurzimmer! Wir freuen uns auf Ihren Besuch.

```html
<!DOCTYPE html>
<html lang="de">
<head>
<meta charset="utf-8">
<title>Flyer Monteursunterkünfte</title>
<link rel="stylesheet" href="https://fonts.googleapis.com/css2?family=Fira+Sans+Condensed:wght@400;700&family=Source+Sans+3:wght@400;600&display=swap">
<style>
  :root {
    --red: #cd1316;
    --ink: #121212;
    --paper: #f6f6f6;
    --shade: #dedede;
    --white: #ffffff;
  }
  * { margin: 0; padding: 0; box-sizing: border-box; }
  html, body { width: 1200px; height: 2400px; overflow: hidden; background: var(--paper); }
  .flyer { position: relative; width: 1200px; height: 2400px; overflow: hidden; background: var(--paper); }
  .diagonal { position: absolute; left: 0; top: 0; width: 1200px; height: 1494px; }
  .headline-box {
    position: absolute; left: 39px; top: 31px; width: 1129px; height: 330px;
    background: var(--red); color: var(--white);
    font-family: "Fira Sans Condensed", sans-serif; font-weight: 400;
    font-size: 53px; line-height: 67px; text-align: center;
    display: flex; flex-direction: column; justify-content: center;
  }
  .headline-box strong { font-weight: 700; }
  .booking {
    position: absolute; left: 0; top: 408px; width: 1200px; text-align: center;
    font-family: "Fira Sans Condensed", sans-serif; font-weight: 700;
    font-size: 48px; line-height: 58px; color: var(--ink);
  }
  .features {
    position: absolute; left: 211px; top: 598px; list-style: none;
    font-family: "Source Sans 3", sans-serif; font-size: 45px; line-height: 54.7px; color: var(--ink);
  }
  .features li::before { content: "• "; }
  .closing {
    position: absolute; left: 0; top: 1043px; width: 1200px; text-align: center;
    font-family: "Source Sans 3", sans-serif; font-size: 55px; line-height: 67px; color: var(--ink);
  }
  .greeting {
    position: absolute; left: 228px; top: 1310px;
    font-family: "Source Sans 3", sans-serif; font-size: 55px; line-height: 67px; color: var(--ink);
  }
  .brand-left {
    position: absolute; left: 20px; top: 1432px;
    font-family: "Source Sans 3", sans-serif; font-weight: 400; font-size: 42px; line-height: 50px;
    letter-spacing: 4px; color: var(--ink);
  }
  .brand-right {
    position: absolute; right: 34px; top: 1390px;
    font-family: "Source Sans 3", sans-serif; font-weight: 600; font-size: 40px; line-height: 48px;
    color: var(--ink);
  }
  .photo {
    position: absolute; left: 0; top: 1494px; width: 1200px; height: 906px;
    background:
      radial-gradient(ellipse 300px 380px at 700px 520px, #b41612 0%, rgba(180,22,18,0) 100%),
      linear-gradient(160deg, #c9ced3 0%, #e4e6e8 45%, #f1f1f1 100%);
  }
</style>
</head>
<body>
<div class="flyer">
  <svg class="diagonal" viewBox="0 0 1200 1494" aria-hidden="true">
    <polygon points="1200,208 1200,1494 179,1494" fill="#dedede"/>
  </svg>

  <div class="headline-box">
    <p>Sie sind auf der Suche nach</p>
    <p>einer <strong>günstigen</strong> und <strong>komfortablen Unterkunft</strong></p>
    <p>für Ihre <strong>Mitarbeiter</strong>?</p>
    <p>Dann sind Sie bei uns genau richtig!</p>
  </div>

  <p class="booking">BUCHEN Sie JETZT SCHNELL und EINFACH: 01629 581706</p>

  <ul class="features">
    <li>Moderne und komfortable Wohnungen</li>
    <li>TV und Kühlschränke auf jedem Zimmer</li>
    <li>Voll ausgestattete Küche</li>
    <li>Immer mit Balkon oder Terrasse</li>
    <li>Kostenloses schnelles W-Lan</li>
    <li>Gute Parkmöglichkeiten</li>
    <li>Willkommenspaket</li>
  </ul>

  <div class="closing">
    <p>Überzeugen Sie sich selbst</p>
    <p>von unserem Angebot und buchen Sie</p>
    <p>noch heute eines unserer Monteurzimmer!</p>
  </div>

  <p class="greeting">Wir freuen uns auf Ihren Besuch.</p>

  <p class="brand-left">QT Dwelling</p>
  <p class="brand-right">RuhOrt17</p>

  <div class="photo" role="img" aria-label="Foto: weiße Kopfkissen und ein rotes Zierkissen auf einem Bett"></div>
</div>
</body>
</html>
```